Harbourlight Campus Lodgings needs a business card design

Hi Guys,

We are a Student Accommodation company in Australia. We already have a logo which I will submit.

I will require the design of the business cards from you.

I am after something that looks clean, modern and that people feel interested and actually want to contact us.

We would like to see designs that are innovative.

On the business cards I will require to have:

Employee Name
Position
Phone number
Email
Facebook page

I hope you can help me with this project guys as I have heard really good things from you.

```html
<!DOCTYPE html>
<html lang="en">
<head>
<meta charset="utf-8">
<title>Harbourlight Campus Lodgings – Business Card</title>
<link href="https://fonts.googleapis.com/css2?family=Lato:wght@400;700;900&display=swap" rel="stylesheet">
<style>
  :root {
    --backdrop: #e9e9e9;
    --card: #ffffff;
    --brand-green: #1e9a43;
    --brand-yellow: #f0b12e;
    --ink: #1c1c1c;
    --muted-grey: #6f6f6f;
    --card-shadow: 0 10px 30px rgba(0,0,0,0.18);
  }
  * { box-sizing: border-box; margin: 0; padding: 0; }
  html, body {
    width: 1200px; height: 926px; overflow: hidden;
    background: var(--backdrop);
    font-family: "Lato", Arial, sans-serif;
    color: var(--ink);
  }
  .sheet {
    width: 1200px; height: 926px;
    display: flex; flex-direction: column;
    align-items: center; justify-content: center; gap: 46px;
  }
  .card {
    position: relative;
    width: 680px; height: 390px;
    background: var(--card);
    box-shadow: var(--card-shadow);
  }

  /* Front */
  .card--front .wordmark {
    position: absolute; left: 250px; top: 120px;
    display: flex; align-items: center; gap: 16px;
  }
  .wordmark__square {
    width: 62px; height: 62px; background: var(--brand-yellow);
  }
  .wordmark__name {
    font-weight: 900; font-size: 27px; line-height: 1.05;
    text-transform: uppercase; letter-spacing: 0.5px;
    color: var(--brand-green);
    width: 200px;
  }
  .card--front .social-link {
    position: absolute; left: 44px; bottom: 70px;
    font-size: 17px; letter-spacing: 0.3px; color: var(--ink);
    white-space: nowrap;
  }

  /* Back */
  .card--back .wordmark {
    position: absolute; left: 40px; top: 150px;
    display: flex; align-items: center; gap: 12px;
  }
  .card--back .wordmark__square { width: 46px; height: 46px; background: #b9b9b9; }
  .card--back .wordmark__name {
    color: var(--muted-grey); font-size: 19px; width: 150px;
  }
  .contact-block { position: absolute; left: 330px; top: 78px; }
  .person-name {
    font-size: 36px; font-weight: 400; color: var(--brand-green); line-height: 1;
    white-space: nowrap;
  }
  .person-name strong { font-weight: 900; }
  .person-title {
    margin-top: 6px;
    font-size: 11px; letter-spacing: 0.6px; text-transform: uppercase;
    color: var(--brand-yellow);
  }
  .contact-list { list-style: none; margin-top: 28px; }
  .contact-list li {
    display: flex; align-items: flex-start; gap: 10px;
    font-size: 16px; line-height: 1.3; margin-bottom: 6px;
  }
  .contact-list svg { flex: none; width: 14px; height: 14px; margin-top: 3px; fill: var(--brand-yellow); }
</style>
</head>
<body>
<main class="sheet">

  <section class="card card--front" aria-label="Card front">
    <div class="wordmark">
      <span class="wordmark__square"></span>
      <span class="wordmark__name">Harbourlight Campus Lodgings</span>
    </div>
    <p class="social-link">mingleboard.net/pages/Harbourlight-Campus-Lodgings/482019375610284</p>
  </section>

  <section class="card card--back" aria-label="Card back">
    <div class="wordmark">
      <span class="wordmark__square"></span>
      <span class="wordmark__name">Harbourlight Campus Lodgings</span>
    </div>
    <div class="contact-block">
      <h1 class="person-name">Nadia <strong>Whitcombe</strong></h1>
      <p class="person-title">Title goes here</p>
      <ul class="contact-list">
        <li>
          <svg viewBox="0 0 16 16" aria-hidden="true"><path d="M3 1h3l1.5 4-2 1.3a9 9 0 0 0 4.2 4.2L11 8.5l4 1.5v3a2 2 0 0 1-2 2A12 12 0 0 1 1 3a2 2 0 0 1 2-2z"/></svg>
          <span>123-456-7890</span>
        </li>
        <li>
          <svg viewBox="0 0 16 16" aria-hidden="true"><path d="M1 3h14v10H1z M2 4l6 5 6-5" fill="none" stroke="#f0b12e" stroke-width="1.6"/></svg>
          <span>yourdomain.com</span>
        </li>
        <li>
          <svg viewBox="0 0 16 16" aria-hidden="true"><path d="M6.5 9.5l3-3M5 7L3 9a2.5 2.5 0 0 0 4 4l2-2M11 9l2-2a2.5 2.5 0 0 0-4-4L7 5" fill="none" stroke="#f0b12e" stroke-width="1.8" stroke-linecap="round"/></svg>
          <span>yourname@yourdomain.com</span>
        </li>
        <li>
          <svg viewBox="0 0 16 16" aria-hidden="true"><path d="M8 1l7 6.5h-2V15h-3.5v-4.5h-3V15H3V7.5H1z"/></svg>
          <span>Street address goes here,<br>Suite #303, Alt Bldg, NY 82365</span>
        </li>
      </ul>
    </div>
  </section>

</main>
</body>
</html>
```